Business Card Design

New business card design

Target Market(s)

Residential & Commercial Property Managers

Industry/Entity Type

Plumbing Services

Contact Information for Business Card

Name - Owen Tredgold, title - Director, Phone Number - 0431 862 507, email - owen@rvb-plumbing.com.au, Company ABN - 73 215 904 386,

Font styles to use
Sans Serif

Colors
0054AA
0677BA
7BADD7
CADEEF
E8F1F8

```html
<!DOCTYPE html>
<html lang="en">
<head>
<meta charset="utf-8">
<title>RVB Plumbing Services – Business Card</title>
<link rel="stylesheet" href="https://fonts.googleapis.com/css2?family=Montserrat:wght@400;700&display=swap">
<style>
  :root {
    --backdrop: #3b3a39;
    --card: #ffffff;
    --ink: #1f2328;
    --muted: #6b625c;
    --blue: #2aa6df;
    --blue-deep: #0677ba;
  }
  * { box-sizing: border-box; margin: 0; padding: 0; }
  html, body { width: 1200px; height: 913px; overflow: hidden; }
  body {
    background: var(--backdrop);
    font-family: "Montserrat", Arial, sans-serif;
    color: var(--ink);
    position: relative;
  }
  .card {
    position: absolute;
    width: 620px;
    height: 354px;
    background: var(--card);
    border-radius: 22px;
    border-bottom: 5px solid var(--blue);
    overflow: hidden;
    box-shadow: 0 18px 40px rgba(0,0,0,.45);
  }
  .card--front { left: 290px; top: 50px; }
  .card--back  { left: 290px; top: 480px; }

  /* wordmark */
  .wordmark {
    display: flex;
    flex-direction: column;
    align-items: center;
    color: var(--ink);
    font-weight: 400;
  }
  .wordmark__name { line-height: 1; letter-spacing: 4px; }
  .wordmark__tag { letter-spacing: 9px; text-transform: lowercase; }

  .card--front .wordmark {
    position: absolute; left: 0; right: 0; top: 92px;
  }
  .card--front .wordmark__name { font-size: 150px; }
  .card--front .wordmark__tag { font-size: 19px; margin-top: 10px; letter-spacing: 14px; }

  .card--back .wordmark {
    position: absolute; left: 30px; top: 78px; width: 250px;
  }
  .card--back .wordmark__name { font-size: 84px; }
  .card--back .wordmark__tag { font-size: 11px; margin-top: 6px; letter-spacing: 7px; }

  .divider {
    position: absolute; left: 300px; top: 42px;
    width: 2px; height: 160px; background: var(--blue);
  }
  .contact { position: absolute; left: 322px; top: 44px; }
  .contact__name { color: var(--blue); font-weight: 700; font-size: 25px; }
  .contact__role { font-size: 17px; margin-top: 2px; }
  .contact__list { list-style: none; margin-top: 18px; font-size: 16px; }
  .contact__list li { display: flex; align-items: center; gap: 8px; margin-bottom: 6px; }
  .contact__list svg { width: 15px; height: 15px; flex: none; }

  .abn-band {
    position: absolute; left: 0; right: 0; top: 238px; height: 38px;
    background: var(--blue);
    color: #fff; font-size: 19px;
    display: flex; align-items: center; padding-left: 70px;
  }
  .abn-band__dot {
    position: absolute; right: 28px; top: 50%;
    width: 26px; height: 26px; margin-top: -13px;
    border-radius: 50%; background: #fff;
  }
  .base-stripe {
    position: absolute; left: 0; right: 0; top: 306px; height: 16px;
    background: var(--blue);
  }
</style>
</head>
<body>
  <section class="card card--front" aria-label="Card front">
    <div class="wordmark">
      <span class="wordmark__name">rvb</span>
      <span class="wordmark__tag">plumbing services</span>
    </div>
  </section>

  <section class="card card--back" aria-label="Card back">
    <div class="wordmark">
      <span class="wordmark__name">rvb</span>
      <span class="wordmark__tag">plumbing services</span>
    </div>
    <div class="divider"></div>
    <div class="contact">
      <p class="contact__name">Owen Tredgold</p>
      <p class="contact__role">Director</p>
      <ul class="contact__list">
        <li>
          <svg viewBox="0 0 24 24" aria-hidden="true"><path fill="var(--blue)" d="M6.6 10.8a15.1 15.1 0 0 0 6.6 6.6l2.2-2.2c.3-.3.7-.4 1-.2 1.1.4 2.3.6 3.6.6.6 0 1 .4 1 1V20c0 .6-.4 1-1 1C10.6 21 3 13.4 3 4c0-.6.4-1 1-1h3.5c.6 0 1 .4 1 1 0 1.3.2 2.5.6 3.6.1.3 0 .7-.2 1z"/></svg>
          0431 862 507
        </li>
        <li>
          <svg viewBox="0 0 24 24" aria-hidden="true"><rect x="2" y="5" width="20" height="14" rx="2" fill="var(--blue)"/><path d="M3 6l9 7 9-7" fill="none" stroke="#fff" stroke-width="1.8"/></svg>
          owen@rvb-plumbing.com.au
        </li>
      </ul>
    </div>
    <div class="abn-band">
      Company ABN - 73 215 904 386
      <span class="abn-band__dot"></span>
    </div>
    <div class="base-stripe"></div>
  </section>
</body>
</html>
```